Website for Healthy Energy Bars

I need the layout for a website that will allow customers to purchase three different energy bars. It should have a slide show of pictures on the front page and the following tabs: About, Nutrition Info, FAQ

The website colors should not conflict with the colors of the company logo. Other than that I am open to design ideas and concepts.

Target Market(s)

Health-Conscious Eaters

Industry/Entity Type

Purchase

Number of Pages Required

3 page

Requirements
Must have
• Logo and pictures of the product
Should not have
• Colors that conflict with the logo colors

```html
<!DOCTYPE html>
<html lang="en">
<head>
<meta charset="utf-8">
<title>Verdabar – Healthy Energy Bars</title>
<link href="https://fonts.googleapis.com/css2?family=Open+Sans:wght@400;600;700;800&display=swap" rel="stylesheet">
<style>
:root{
  --green:#8dc63f;
  --green-dark:#6ea52a;
  --maroon:#5b1028;
  --footer:#2b0b16;
  --ink:#333333;
  --muted:#888888;
  --line:#e3e3e3;
  --hero-bg:#eeeeee;
  --white:#ffffff;
}
*{box-sizing:border-box;margin:0;padding:0}
html,body{width:841px;height:1200px;overflow:hidden;background:var(--white)}
body{font-family:"Open Sans",Arial,sans-serif;color:var(--ink);position:relative}
a{color:inherit;text-decoration:none}

/* header */
.site-header{position:absolute;top:0;left:0;width:841px;height:112px;background:var(--white)}
.header-swoosh{position:absolute;top:0;left:0}
.brand{position:absolute;left:40px;top:36px;display:flex;align-items:center;gap:7px}
.brand-dot{width:14px;height:14px;border-radius:50%;background:var(--white)}
.brand-name{font-size:24px;font-weight:800;color:var(--white);letter-spacing:-.3px;line-height:1}
.util-links{position:absolute;top:8px;right:185px;font-size:9px;color:var(--muted);display:flex;gap:10px}
.search{position:absolute;top:5px;right:30px;width:145px;height:18px;border:1px solid var(--line);font-size:9px;color:#aaa;padding:2px 6px}
.main-nav{position:absolute;top:66px;right:205px;display:flex;gap:26px;font-size:12px;font-weight:600}
.cart{position:absolute;top:58px;right:30px;display:flex;align-items:center;gap:8px;font-size:12px;font-weight:700}
.cart-icon{width:28px;height:28px;border-radius:50%;background:var(--green);display:flex;align-items:center;justify-content:center}

/* hero */
.hero{position:absolute;top:112px;left:0;width:841px;height:282px;background:var(--hero-bg);overflow:hidden}
.hero-curve{position:absolute;right:0;top:0}
.hero-title{position:absolute;left:28px;top:22px;font-size:40px;font-weight:800;line-height:1.05;color:var(--ink);width:420px}
.hero-sub{position:absolute;left:28px;top:118px;font-size:14px;font-weight:600;color:var(--green-dark);width:360px;line-height:1.3}
.btn{display:inline-block;background:var(--maroon);color:var(--white);font-size:10px;font-weight:700;padding:8px 14px}
.hero .btn{position:absolute;left:28px;top:178px}
.dots{position:absolute;left:28px;top:235px;display:flex;gap:6px}
.dots span{width:9px;height:9px;border-radius:50%;background:#bbb}
.dots span:first-child{background:var(--ink)}
.hero-photo{position:absolute;left:455px;top:20px;width:360px;height:245px;border-radius:4px;background:linear-gradient(135deg,#ffffff,#dfe9cf 55%,#b48a5a)}

/* products */
.products{position:absolute;top:402px;left:28px;width:785px}
.section-title{font-size:19px;font-weight:700;color:var(--ink)}
.product-row{display:flex;gap:18px;margin-top:26px}
.product-card{width:183px;border:1px solid var(--line);position:relative;padding-top:32px}
.product-card::before{content:"";position:absolute;top:0;left:0;right:0;height:26px;background:var(--green);clip-path:polygon(0 0,100% 0,100% 30%,0 100%)}
.product-photo{width:110px;height:62px;margin:0 auto;border-radius:3px;background:linear-gradient(135deg,#ffffff,#dfe9cf 60%,#a57d52);border:1px solid var(--line)}
.product-name{text-align:center;font-size:11px;font-weight:700;margin-top:8px}
.product-desc{text-align:center;font-size:7.5px;color:var(--muted);width:130px;margin:3px auto 0;line-height:1.3}
.price{text-align:center;color:var(--green-dark);font-size:17px;font-weight:700;margin:8px 0}
.card-actions{display:flex;justify-content:space-between;align-items:center;border-top:1px solid var(--line)}
.add-cart{font-size:9px;font-weight:700;padding-left:10px}
.cart-btn{width:36px;height:30px;background:var(--maroon);display:flex;align-items:center;justify-content:center}

/* nutrition band */
.nutrition{position:absolute;top:712px;left:0;width:841px;height:160px;background:var(--green)}
.nutrition-title{position:absolute;left:28px;top:20px;color:var(--white);font-size:19px;font-weight:700}
.nutrition-text{position:absolute;left:28px;top:52px;width:470px;color:var(--white);font-size:9px;line-height:1.5}
.nutrition .btn{position:absolute;left:28px;top:108px}
.nutrition-photo{position:absolute;left:525px;top:-38px;width:290px;height:185px;border-radius:4px;background:linear-gradient(135deg,#ffffff,#e3ecd3 55%,#b48a5a)}

/* features */
.features{position:absolute;top:898px;left:28px;width:785px;display:flex;gap:22px}
.feature{flex:1;height:106px;border:1px solid var(--line);display:flex;align-items:center;justify-content:center;gap:12px;font-size:14px;font-weight:700}
.feature-icon{width:42px;height:42px;border-radius:50%;border:3px solid var(--green);display:flex;align-items:center;justify-content:center}

/* footer */
.site-footer{position:absolute;top:1030px;left:0;width:841px;height:170px;background:var(--footer);color:#cfc4c8;overflow:hidden}
.footer-leaf{position:absolute;left:0;top:0;width:200px;height:170px;background:radial-gradient(circle at 30% 30%,rgba(141,198,63,.15),transparent 70%)}
.footer-brand{position:absolute;left:40px;top:36px;font-size:26px;font-weight:800;color:var(--green)}
.copyright{position:absolute;left:40px;top:84px;font-size:8px;line-height:1.5;width:150px}
.footer-col{position:absolute;top:16px;font-size:8.5px;line-height:1.75}
.footer-col h4{color:var(--green);font-size:11px;font-weight:700;margin-bottom:4px}
.social{display:flex;gap:6px;margin-top:4px}
.social span{width:20px;height:20px;border-radius:50%;border:1px solid #cfc4c8}
.to-top{position:absolute;right:14px;bottom:12px;width:18px;height:14px;background:var(--green)}
</style>
</head>
<body>

<header class="site-header">
  <svg class="header-swoosh" width="320" height="112" viewBox="0 0 320 112" aria-hidden="true">
    <path d="M0 0 H315 C285 60 200 98 0 110 Z" fill="#8dc63f"/>
  </svg>
  <a class="brand" href="#"><span class="brand-dot"></span><span class="brand-name">Verdabar</span></a>
  <div class="util-links"><span>Login</span><span>|</span><span>Register</span><span>|</span><span>My Account</span><span>|</span><span>Wishlist</span></div>
  <div class="search">Search</div>
  <nav class="main-nav"><a href="#">Home</a><a href="#">About</a><a href="#">Nutrition Info</a><a href="#">FAQ</a><a href="#">Contact</a></nav>
  <div class="cart">
    <span class="cart-icon"><svg width="14" height="14" viewBox="0 0 24 24"><path d="M3 4h3l2 11h11l2-8H7" fill="none" stroke="#fff" stroke-width="2.4"/><circle cx="9" cy="19" r="1.8" fill="#fff"/><circle cx="18" cy="19" r="1.8" fill="#fff"/></svg></span>
    <span>My Cart: $0.00</span>
  </div>
</header>

<section class="hero">
  <svg class="hero-curve" width="420" height="282" viewBox="0 0 420 282" aria-hidden="true">
    <path d="M420 0 V282 H180 C300 240 380 150 420 0 Z" fill="#8dc63f"/>
  </svg>
  <h1 class="hero-title">Vestibulum ante ipsum primis</h1>
  <p class="hero-sub">Suspendisse lobortis turpis in odio blandit ac interdum lorem euismod.</p>
  <a class="btn" href="#">SHOP NOW</a>
  <div class="dots"><span></span><span></span><span></span><span></span></div>
  <div class="hero-photo" role="img" aria-label="Photo of an open box of energy bars"></div>
</section>

<section class="products">
  <h2 class="section-title">Our Products</h2>
  <div class="product-row">
    <article class="product-card">
      <div class="product-photo" role="img" aria-label="Energy bar box photo"></div>
      <h3 class="product-name">PRODUCT NAME</h3>
      <p class="product-desc">Duis aliquam nibh a dui iaculis viverra id a velit</p>
      <p class="price">$0.00</p>
      <div class="card-actions"><span class="add-cart">ADD TO CART</span><span class="cart-btn"><svg width="14" height="14" viewBox="0 0 24 24"><path d="M3 4h3l2 11h11l2-8H7" fill="none" stroke="#fff" stroke-width="2.4"/><circle cx="9" cy="19" r="1.8" fill="#fff"/><circle cx="18" cy="19" r="1.8" fill="#fff"/></svg></span></div>
    </article>
    <article class="product-card">
      <div class="product-photo" role="img" aria-label="Energy bar box photo"></div>
      <h3 class="product-name">PRODUCT NAME</h3>
      <p class="product-desc">Duis aliquam nibh a dui iaculis viverra id a velit</p>
      <p class="price">$0.00</p>
      <div class="card-actions"><span class="add-cart">ADD TO CART</span><span class="cart-btn"><svg width="14" height="14" viewBox="0 0 24 24"><path d="M3 4h3l2 11h11l2-8H7" fill="none" stroke="#fff" stroke-width="2.4"/><circle cx="9" cy="19" r="1.8" fill="#fff"/><circle cx="18" cy="19" r="1.8" fill="#fff"/></svg></span></div>
    </article>
    <article class="product-card">
      <div class="product-photo" role="img" aria-label="Energy bar box photo"></div>
      <h3 class="product-name">PRODUCT NAME</h3>
      <p class="product-desc">Duis aliquam nibh a dui iaculis viverra id a velit</p>
      <p class="price">$0.00</p>
      <div class="card-actions"><span class="add-cart">ADD TO CART</span><span class="cart-btn"><svg width="14" height="14" viewBox="0 0 24 24"><path d="M3 4h3l2 11h11l2-8H7" fill="none" stroke="#fff" stroke-width="2.4"/><circle cx="9" cy="19" r="1.8" fill="#fff"/><circle cx="18" cy="19" r="1.8" fill="#fff"/></svg></span></div>
    </article>
    <article class="product-card">
      <div class="product-photo" role="img" aria-label="Energy bar box photo"></div>
      <h3 class="product-name">PRODUCT NAME</h3>
      <p class="product-desc">Duis aliquam nibh a dui iaculis viverra id a velit</p>
      <p class="price">$0.00</p>
      <div class="card-actions"><span class="add-cart">ADD TO CART</span><span class="cart-btn"><svg width="14" height="14" viewBox="0 0 24 24"><path d="M3 4h3l2 11h11l2-8H7" fill="none" stroke="#fff" stroke-width="2.4"/><circle cx="9" cy="19" r="1.8" fill="#fff"/><circle cx="18" cy="19" r="1.8" fill="#fff"/></svg></span></div>
    </article>
  </div>
</section>

<section class="nutrition">
  <h2 class="nutrition-title">Nutrition Info</h2>
  <p class="nutrition-text">Aenean mi nisl, feugiat vel lacus ut, semper euismod nisi. Integer varius diam vel neque commodo, sit amet tempor augue porta. Suspendisse fermentum tincidunt sem, vitae pulvinar lorem dictum in. Nunc ut faucibus arcu.</p>
  <a class="btn" href="#">READ MORE</a>
  <div class="nutrition-photo" role="img" aria-label="Photo of an open box of energy bars"></div>
</section>

<section class="features">
  <div class="feature"><span class="feature-icon"><svg width="20" height="20" viewBox="0 0 24 24"><path d="M4 5h16v10H9l-5 4z" fill="none" stroke="#8dc63f" stroke-width="2.2"/></svg></span>Customer Supports</div>
  <div class="feature"><span class="feature-icon"><svg width="20" height="20" viewBox="0 0 24 24"><path d="M2 7h12v9H2zM14 10h4l3 3v3h-7z" fill="none" stroke="#8dc63f" stroke-width="2"/><circle cx="6" cy="18" r="2" fill="#8dc63f"/><circle cx="17" cy="18" r="2" fill="#8dc63f"/></svg></span>FREE Shipping</div>
  <div class="feature"><span class="feature-icon"><svg width="20" height="20" viewBox="0 0 24 24"><rect x="3" y="6" width="18" height="12" fill="none" stroke="#8dc63f" stroke-width="2.2"/><path d="M3 6l9 7 9-7" fill="none" stroke="#8dc63f" stroke-width="2.2"/></svg></span>Newsletter SignUp</div>
</section>

<footer class="site-footer">
  <div class="footer-leaf" role="img" aria-label="Faint leaf decoration"></div>
  <div class="footer-brand">Verdabar</div>
  <p class="copyright">Copyright © 2015, Company Name. All Rights Reserved.</p>
  <div class="footer-col" style="left:255px"><h4>Navigation</h4>Home<br>About<br>Nutrition Info<br>FAQ<br>Contact</div>
  <div class="footer-col" style="left:385px"><h4>Support</h4>Duis aliquam<br>Nibh a dui iaculis<br>Viverra id a velit<br>Iaculis egestas</div>
  <div class="footer-col" style="left:515px"><h4>Policy</h4>Duis aliquam<br>Nibh a dui iaculis<br>Viverra id a velit<br>Iaculis egestas</div>
  <div class="footer-col" style="left:650px"><h4>Connect Us</h4><div class="social"><span></span><span></span><span></span><span></span></div></div>
  <span class="to-top"></span>
</footer>

</body>
</html>
```